Yearly symposium in equestrian ethology needs a poster

We need a poster for a Yearly symposium in equestrian ethology. Ethology = science which studies animal behaviours. In our case horses behaviours.
Our principal and basic thematic is "the contribution of the ethology to the human-horse relationship".
This poster wil have to be a lay out which will be used each year with an update of the content, photos following the theme.
the original file, fonts or other graphics will have to be provided with the final project. Do not forget that you will probably design it in english and we will have to translate it in french.
Through this visual we want to communicate: science, rigorous, relationship, respect and wellness of horses and human - harmony. We want to encourage critical thinking.
This year the theme will be "is the horse a therapist?"

Enclosed you will find the poster for the symposium 2013

The final amount will have to be invoiced.
Updates

Reason: I will be on vacation from Aug 12 till 19. I'll give feedback to your projects and posted comments when I return

Target Market(s)

Anyone wanting to improve their relationship with horses. Most of participnats are women but not only. Age: between 20 and 50.

Industry/Entity Type

Wellness

Requirements
Must have
• Place to add pratical info: date, place, title of the symposium etc.

```html
<!DOCTYPE html>
<html lang="en">
<head>
<meta charset="utf-8">
<title>Equine Ethology Symposium</title>
<link rel="stylesheet" href="https://fonts.googleapis.com/css2?family=Tinos:wght@400;700&display=swap">
<style>
  :root {
    --orange-deep: #e0852a;
    --orange: #ec9a40;
    --orange-light: #f6bd78;
    --cream: #fbe3c4;
    --ink: #2a1708;
    --white: #ffffff;
    --photo-light: #c9c6c0;
    --photo-dark: #2c2a28;
  }
  * { margin: 0; padding: 0; box-sizing: border-box; }
  html, body { width: 848px; height: 1200px; overflow: hidden; background: var(--white); }
  .poster {
    position: relative;
    width: 848px;
    height: 1200px;
    overflow: hidden;
    font-family: "Tinos", "Times New Roman", serif;
    color: var(--ink);
    background: linear-gradient(180deg, var(--orange-light) 0%, var(--orange) 18%, var(--orange-deep) 100%);
  }
  .backdrop { position: absolute; inset: 0; }
  .brand {
    position: absolute;
    left: 19px; top: 37px;
    width: 90px; height: 114px;
    background: var(--white);
    display: flex; flex-direction: column; align-items: center; justify-content: center; gap: 10px;
  }
  .brand-mark { width: 34px; height: 34px; border: 3px solid var(--ink); border-radius: 50%; }
  .brand-name { font-size: 16px; font-weight: 400; color: var(--ink); }
  .header { position: absolute; left: 130px; right: 20px; top: 54px; text-align: center; }
  .event-title { font-size: 44px; font-weight: 400; line-height: 1; }
  .event-date { font-size: 26px; margin-top: 14px; line-height: 1.1; }
  .event-venue { font-size: 19px; margin-top: 8px; }
  .event-address { font-size: 19px; margin-top: 8px; }
  .programme { position: absolute; left: 0; right: 0; top: 876px; text-align: center; }
  .lead { font-size: 19px; line-height: 1.5; }
  .theme { font-size: 28px; font-weight: 700; margin-top: 12px; }
  .topics { font-size: 16.5px; margin-top: 8px; line-height: 1.45; }
  .speakers { list-style: none; font-size: 16.5px; line-height: 1.45; }
  .speakers small { font-size: 12.5px; }
  .fees { font-size: 14.5px; margin-top: 4px; }
  .info { font-size: 14.5px; margin-top: 8px; }
  .info strong { font-weight: 700; }
</style>
</head>
<body>
<main class="poster">
  <svg class="backdrop" width="848" height="1200" viewBox="0 0 848 1200">
    <defs>
      <linearGradient id="photoTone" x1="0" y1="0" x2="1" y2="0.3">
        <stop offset="0" stop-color="var(--photo-light)"/>
        <stop offset="0.45" stop-color="#8d8a86"/>
        <stop offset="0.65" stop-color="var(--photo-dark)"/>
        <stop offset="1" stop-color="#4a4642"/>
      </linearGradient>
    </defs>
    <path class="band-light" d="M0 225 C 220 210, 420 290, 848 250 L 848 330 C 560 330, 300 250, 0 300 Z" fill="var(--cream)" opacity="0.85"/>
    <path class="band-white" d="M0 245 C 240 235, 430 300, 848 275 L 848 320 C 560 330, 300 260, 0 290 Z" fill="var(--white)"/>
    <path class="photo-area" role="img" aria-label="Close-up of a grey horse's eye beside its bridle"
      d="M0 290 C 300 255, 560 330, 848 318 L 848 650 C 700 640, 620 780, 420 820 C 260 850, 120 840, 0 865 Z"
      fill="url(#photoTone)"/>
    <path class="band-swoosh" d="M0 865 C 140 838, 280 852, 430 818 C 620 778, 700 640, 848 650 L 848 690 C 700 690, 620 820, 430 855 C 280 882, 140 865, 0 895 Z" fill="var(--orange-light)" opacity="0.7"/>
  </svg>

  <div class="brand">
    <span class="brand-mark"></span>
    <span class="brand-name">Valmont</span>
  </div>

  <header class="header">
    <h1 class="event-title">Equine Ethology Symposium</h1>
    <p class="event-date">Saturday 29 March 2014, 8:30 am to 6:00 pm</p>
    <p class="event-venue">University of Valmont</p>
    <p class="event-address">Valmont, Auditorium CH01, Faculty of Sciences, rue Lemaire</p>
  </header>

  <section class="programme">
    <p class="lead">The contribution of ethology to the human-horse relationship<br>2014 Edition:</p>
    <h2 class="theme">“Is the horse a therapist?”</h2>
    <p class="topics">Horse-assisted therapy: evidence and limits,…<br>Wellbeing of horse and human in the relationship</p>
    <ul class="speakers">
      <li>Elke Vandermolen, <small>Hoogveld University, Netherlands</small></li>
      <li>Luc Dorval, <small>Meerhout University</small></li>
      <li>Paul Verstraete, <small>Faculty of Veterinary Medicine, Ardenval</small></li>
    </ul>
    <p class="fees">Fees: adults €50 (€60 on site) – students €25 (€30 on site). Lunch included – limited seating.</p>
    <p class="info">Information and registration: <strong>www.colloque-equin.be</strong></p>
  </section>
</main>
</body>
</html>
```